I need a website built for my organization.
We are the world's largest network of music producers.
The website should be professional, sharp, and high quality., We need a website built for The Halvern Sound Guild. We are one of the World's largest association of music producers.
The site must be professional, sharp, and high quality., I need a website built for my organization.
The site must be professional, sharp, and high quality.
Somewhere in the top half of the site there should be a form for the user to fill out. The details of the form are as follows:
Title (large and bold): Contact Us or Submit Your Music
Fields to include (* = required): First Name*, Last Name*, Age, Zip Code, Email Address*, Daytime Phone, Evening Phone, Comments
Then, there will be a "submit" button to proceed to next step of form. Just below the "submit" button, should be the following verbiage: "After submitting, you will have the opportunity to upload demos of your music (optional) and provide other pertinent information about yourself, band, or group."
Target Market(s)
Music producers and aspiring musicians
Industry/Entity Type
Group
Colors
Designer to choose colors to be used in the design.
Look and feel

```html
<!DOCTYPE html>
<html lang="en">
<head>
<meta charset="utf-8">
<title>The Halvern Sound Guild — Contact &amp; Submit</title>
<link rel="stylesheet" href="https://fonts.googleapis.com/css2?family=Archivo:wght@400;500;800&family=Source+Sans+3:wght@400&family=Playfair+Display:ital,wght@1,700&display=swap">
<style>
  :root {
    --ink: #000000;
    --studio-deep: #05040c;
    --studio-violet: #3a2270;
    --studio-magenta: #8a2a5a;
    --studio-amber: #7a6a10;
    --white: #ffffff;
    --field-text: #1c1c1c;
    --guild-pink: #e45a93;
    --player-blue: #3c35cc;
    --contact-red: #c43a2e;
    --submit-green: #27ae5f;
  }
  * { box-sizing: border-box; margin: 0; padding: 0; }
  html, body { width: 1200px; height: 960px; overflow: hidden; background: var(--ink); }
  .page {
    position: relative; width: 1200px; height: 960px; overflow: hidden;
    font-family: "Archivo", Arial, sans-serif; color: var(--white);
  }
  .studio-backdrop {
    position: absolute; inset: 0;
    background:
      radial-gradient(ellipse 420px 200px at 330px 580px, rgba(138,42,90,.55), transparent 70%),
      radial-gradient(ellipse 300px 260px at 160px 420px, rgba(58,34,112,.5), transparent 70%),
      radial-gradient(ellipse 260px 360px at 1120px 420px, rgba(122,106,16,.55), transparent 70%),
      radial-gradient(ellipse 260px 180px at 90px 760px, rgba(150,150,160,.35), transparent 70%),
      linear-gradient(160deg, var(--studio-deep) 0%, #0b0812 60%, var(--ink) 100%);
  }
  .brand {
    position: absolute; left: 122px; top: 44px;
    display: flex; align-items: center; gap: 12px;
    font-weight: 500; font-size: 24px; color: var(--guild-pink); letter-spacing: .2px;
  }
  .brand-dot { width: 34px; height: 34px; border-radius: 50%; background: var(--player-blue); }
  .section-title { text-transform: uppercase; line-height: .78; }
  .section-title .light { display: block; font-weight: 400; }
  .section-title .bold { display: block; font-weight: 800; }
  .recent { position: absolute; left: 122px; top: 246px; }
  .recent .section-title { font-size: 45px; }
  .track-name { margin-top: 28px; font-size: 17px; }
  .track-artist { margin-top: 2px; font-size: 12.5px; }
  .progress { margin-top: 10px; width: 290px; height: 8px; background: var(--white); }
  .progress-fill { width: 127px; height: 100%; background: var(--player-blue); }
  .controls { margin-top: 12px; display: flex; align-items: center; gap: 9px; }
  .ctrl { display: block; }
  .contact-btn {
    position: absolute; left: 607px; top: 28px; width: 234px; height: 56px;
    background: var(--contact-red); color: var(--white); border: 0;
    font: 800 28px "Archivo", Arial, sans-serif; text-transform: uppercase;
    display: flex; align-items: center; justify-content: center;
  }
  .divider {
    position: absolute; left: 607px; top: 104px; width: 234px;
    display: flex; align-items: center; gap: 12px;
    font: italic 700 24px "Playfair Display", Georgia, serif;
  }
  .divider::before, .divider::after { content: ""; flex: 1; height: 2px; background: var(--white); }
  .submit-form { position: absolute; left: 607px; top: 152px; }
  .submit-form .section-title { font-size: 45px; }
  .fields {
    margin-top: 30px; display: grid; grid-template-columns: 230px 230px;
    column-gap: 14px; row-gap: 14px;
  }
  .field {
    height: 47px; border: 0; background: var(--white); padding: 0 13px;
    font: 400 18px "Source Sans 3", Arial, sans-serif; color: var(--field-text);
  }
  .field::placeholder { color: var(--field-text); opacity: 1; }
  .field-comment { grid-column: 1 / 3; height: 131px; padding-top: 13px; resize: none; }
  .submit-btn {
    margin-top: 20px; width: 234px; height: 56px; border: 0;
    background: var(--submit-green); color: var(--white);
    font: 800 30px "Archivo", Arial, sans-serif; text-transform: uppercase;
  }
</style>
</head>
<body>
<main class="page">
  <div class="studio-backdrop" role="img" aria-label="Dark recording studio with a microphone on a boom arm, pop filter and acoustic foam lit in violet, magenta and amber"></div>

  <div class="brand"><span class="brand-dot"></span>The Halvern Sound Guild</div>

  <section class="recent">
    <h2 class="section-title"><span class="light">Most</span><span class="bold">Recent</span></h2>
    <p class="track-name">Neon Drift</p>
    <p class="track-artist">Velour Static</p>
    <div class="progress"><div class="progress-fill"></div></div>
    <div class="controls">
      <svg class="ctrl" width="30" height="30" viewBox="0 0 30 30" aria-label="Previous"><circle cx="15" cy="15" r="15" fill="var(--player-blue)"/><rect x="10" y="10.5" width="2" height="9" fill="#fff"/><path d="M20 10.5v9l-7-4.5z" fill="#fff"/></svg>
      <svg class="ctrl" width="52" height="52" viewBox="0 0 52 52" aria-label="Play"><circle cx="26" cy="26" r="26" fill="var(--player-blue)"/><path d="M20 16v20l16-10z" fill="#fff"/></svg>
      <svg class="ctrl" width="30" height="30" viewBox="0 0 30 30" aria-label="Next"><circle cx="15" cy="15" r="15" fill="var(--player-blue)"/><path d="M10 10.5v9l7-4.5z" fill="#fff"/><rect x="18" y="10.5" width="2" height="9" fill="#fff"/></svg>
    </div>
  </section>

  <a class="contact-btn" href="#contact">Contact Us</a>
  <div class="divider">or</div>

  <form class="submit-form" id="contact">
    <h1 class="section-title"><span class="light">Submit</span><span class="bold">Your Music</span></h1>
    <div class="fields">
      <input class="field" type="text" placeholder="First Name" required>
      <input class="field" type="text" placeholder="Last Name" required>
      <input class="field" type="text" placeholder="Age">
      <input class="field" type="text" placeholder="Zip Code">
      <input class="field" type="email" placeholder="Email Address" required>
      <span></span>
      <input class="field" type="tel" placeholder="Daytime Phone">
      <input class="field" type="tel" placeholder="Evening Phone">
      <textarea class="field field-comment" placeholder="Comment"></textarea>
    </div>
    <button class="submit-btn" type="submit">Submit</button>
  </form>
</main>
</body>
</html>
```